Post card for landscape service

Velmora Property Management**FEATURED SERVICE*** Weekly Lawn mowing service starting at $15/ cutting ****other services****landscape servicespring and fall clean uplawn and flowerbed care (pest and weed control)fertilizing plantingand moreCall for a Free estimate!!10% off first months service with signed contract

Please make double sided ( a front and a back)

Target Market(s)

home owners

Industry/Entity Type

Landscape

Requirements
Must have
• please feture the weekly lawn mowing service and then list the other sevices
• contact info... can be found on business card that was uploaded.
• must say residential services
Should not have
• please dont list reo management

```html
<!DOCTYPE html>
<html lang="en">
<head>
<meta charset="UTF-8">
<title>Velmora Property Management – Postcard</title>
<link rel="stylesheet" href="https://fonts.googleapis.com/css2?family=Montserrat:wght@600;700;800;900&family=Questrial&display=swap">
<style>
  :root{
    --bg:#2e2e30;
    --green:#4a9e2f;
    --green-light:#7cc043;
    --green-dark:#2f7a1e;
    --ink:#3c3c3c;
    --grey:#555;
    --red:#d7262b;
    --white:#ffffff;
    --panel:rgba(255,255,255,0.88);
    --line:#c9c9c9;
  }
  *{box-sizing:border-box;margin:0;padding:0}
  html,body{width:1200px;height:1026px;overflow:hidden;background:var(--bg)}
  body{position:relative;font-family:"Questrial",sans-serif;color:var(--ink)}
  .postcard{position:absolute;left:240px;width:720px;height:480px;background:var(--white);overflow:hidden;box-shadow:0 8px 24px rgba(0,0,0,.45)}
  .postcard--front{top:22px}
  .postcard--back{top:524px}

  /* FRONT */
  .front-photo{position:absolute;inset:0;background:linear-gradient(180deg,#b9c5cf 0%,#9aa39a 30%,#6f8a4d 55%,#4f8f2c 75%,#5fa336 100%)}
  .front-banner{position:absolute;right:24px;top:18px;width:360px;height:96px;background:linear-gradient(135deg,var(--green-light),var(--green-dark));clip-path:polygon(0 0,100% 0,100% 78%,52% 78%,44% 100%,36% 78%,0 78%);color:var(--white);text-align:center;font-family:"Montserrat",sans-serif;padding-top:6px}
  .front-banner .headline{font-weight:900;font-size:24px;line-height:1;letter-spacing:.5px}
  .front-banner .sub{font-weight:700;font-size:16px;margin-top:2px}
  .front-panel{position:absolute;right:24px;top:112px;width:360px;height:348px;background:var(--panel);text-align:center;padding:14px 18px}
  .brand{display:flex;flex-direction:column;align-items:center}
  .brand-dot{width:40px;height:40px;border-radius:50%;background:var(--ink);margin-bottom:8px}
  .brand-name{font-size:38px;color:var(--green);line-height:1;letter-spacing:1px}
  .brand-tag{font-size:20px;color:var(--grey);letter-spacing:.5px;margin-top:2px}
  .services-line{color:var(--green);font-size:17px;line-height:1.3;margin-top:12px}
  .cta{font-size:24px;color:var(--ink);margin-top:12px}
  .phone-big{font-family:"Montserrat",sans-serif;font-weight:800;font-size:46px;color:var(--green);line-height:1.1}
  .offer{color:var(--red);font-size:14px;margin-top:4px}

  /* BACK */
  .back-left{position:absolute;left:0;top:0;width:440px;height:480px;background:linear-gradient(180deg,#f4f7f1 0%,#eef3ea 60%,#e4ecdf 100%)}
  .back-photo{position:absolute;left:0;top:0;width:290px;height:130px;background:linear-gradient(135deg,#e6ded0 0%,#8caa5a 40%,#d44c8a 70%,#4a7d2e 100%)}
  .back-blurb{position:absolute;left:290px;top:0;width:150px;height:130px;background:rgba(74,158,47,.9);color:var(--white);font-family:"Montserrat",sans-serif;font-weight:700;font-size:11px;line-height:1.3;padding:10px}
  .services-head{position:absolute;left:20px;top:146px;font-family:"Montserrat",sans-serif;font-weight:800;font-size:22px;color:var(--green)}
  .services-intro{position:absolute;left:20px;top:174px;width:400px;font-family:"Montserrat",sans-serif;font-weight:700;font-size:11.5px;line-height:1.25;color:var(--ink)}
  .service-list{position:absolute;left:24px;top:224px;list-style:none;font-size:14px;line-height:1.45;color:var(--ink)}
  .service-list li::before{content:"";display:inline-block;width:7px;height:7px;border-radius:50%;background:var(--green-light);margin-right:10px;vertical-align:middle}
  .round-photo{position:absolute;width:84px;height:84px;border-radius:50%;border:4px solid var(--white);box-shadow:0 1px 4px rgba(0,0,0,.3)}
  .round-photo--building{left:300px;top:206px;background:linear-gradient(180deg,#b43a2f 0%,#8d9e7c 60%,#4f8f2c 100%)}
  .round-photo--snow{left:336px;top:268px;background:linear-gradient(180deg,#dfe3e6 0%,#b9bfc4 60%,#8a3b33 100%)}
  .web-bar{position:absolute;left:0;top:378px;width:440px;height:30px;background:var(--green);color:var(--white);font-family:"Montserrat",sans-serif;font-weight:700;font-size:16px;letter-spacing:.5px;display:flex;align-items:center;justify-content:center}
  .address{position:absolute;left:20px;top:420px;font-size:15px;line-height:1.3;color:var(--grey)}
  .contact{position:absolute;left:236px;top:414px;font-size:14px;line-height:1.5;color:var(--grey)}
  .contact div{display:flex;align-items:center;gap:6px}
  .contact svg{width:14px;height:14px;fill:var(--green)}
  .back-right{position:absolute;left:440px;top:0;width:280px;height:480px}
  .stamp-box{position:absolute;right:26px;top:24px;width:62px;height:56px;background:#e6e6e6}
  .address-lines{position:absolute;left:30px;right:26px;top:190px}
  .address-lines span{display:block;height:1px;background:var(--line);margin-bottom:34px}
</style>
</head>
<body>

<section class="postcard postcard--front" aria-label="Postcard front">
  <div class="front-photo" role="img" aria-label="Photo of a suburban house with a green lawn, shrubs and red flower beds"></div>
  <div class="front-banner">
    <div class="headline">WEEKLY LAWN<br>MOWING SERVICE</div>
    <div class="sub">starting at $15/ cutting</div>
  </div>
  <div class="front-panel">
    <div class="brand">
      <span class="brand-dot"></span>
      <div class="brand-name">VELMORA</div>
      <div class="brand-tag">PROPERTY MANAGEMENT</div>
    </div>
    <p class="services-line">Commercial and Residential<br>Property Management Services</p>
    <p class="cta">Call for a Free estimate!!</p>
    <p class="phone-big">908-555-0176</p>
    <p class="offer">10% off first months service with signed contract</p>
  </div>
</section>

<section class="postcard postcard--back" aria-label="Postcard back">
  <div class="back-left">
    <div class="back-photo" role="img" aria-label="Photo of a front garden with pink flowers and green shrubs"></div>
    <p class="back-blurb">Velmora Property Management will help you manage your properties with services ranging from landscaping, pest control, snow removal and more.</p>
    <h2 class="services-head">SERVICES</h2>
    <p class="services-intro">Velmora Property Managment offers a wide veriety of services that will keep your facility looking good and operating even better.</p>
    <ul class="service-list">
      <li>Landscape Service</li>
      <li>Spring And Fall Clean Up</li>
      <li>Lawn And Flower</li>
      <li>Bed Care (Pest And Weed Control)</li>
      <li>Fertilizing Planting</li>
      <li>And More</li>
    </ul>
    <div class="round-photo round-photo--building" role="img" aria-label="Photo of a brick commercial building with landscaped lawn"></div>
    <div class="round-photo round-photo--snow" role="img" aria-label="Photo of a snow-covered parking area after snow removal"></div>
    <div class="web-bar">www.velmorapropertymanagement.com</div>
    <p class="address">PO Box 418<br>Fernbrook, NJ 08990</p>
    <div class="contact">
      <div><svg viewBox="0 0 24 24" aria-hidden="true"><path d="M6.6 10.8a15.1 15.1 0 0 0 6.6 6.6l2.2-2.2a1 1 0 0 1 1-.25 11.4 11.4 0 0 0 3.6.57 1 1 0 0 1 1 1V20a1 1 0 0 1-1 1A17 17 0 0 1 3 4a1 1 0 0 1 1-1h3.5a1 1 0 0 1 1 1c0 1.25.2 2.45.57 3.57a1 1 0 0 1-.25 1z"/></svg>908-555-0176</div>
      <div><svg viewBox="0 0 24 24" aria-hidden="true"><path d="M2 5h20v14H2z M2 5l10 8 10-8" fill="none" stroke="#4a9e2f" stroke-width="2"/></svg>velmoraproperty@mail.com</div>
    </div>
  </div>
  <div class="back-right">
    <div class="stamp-box"></div>
    <div class="address-lines"><span></span><span></span><span></span><span></span><span></span><span></span></div>
  </div>
</section>

</body>
</html>
```